business cards foreign exchange student company
Bluebird Hosting
Bright & Fun-filled
Mack Dorran
Service Director
Western Region
mack@mybluebirdhosting.com
mybluebirdhosting.com
This business card needs to be unforgettable! It needs to stand out from all the other business cards. Something clever/funny. It needs to communicate this is fun!! this is exciting!! and our theme for our company is "The Best Time Ever!" so the business card should convey that they have just found The Best Time Ever!!!
This will be my new website (with the old logo)
this is a marketing piece used to send families to the website
another marketing piece to get families to the website
This is my logo .ai file
This is my .ai logo file for dark backgrounds

```html
<!DOCTYPE html>
<html lang="en">
<head>
<meta charset="utf-8">
<title>Bluebird Hosting – Business Card</title>
<link rel="stylesheet" href="https://fonts.googleapis.com/css2?family=Lora:wght@400;700&display=swap">
<style>
  :root {
    --bg: #2b2b2d;
    --card-white: #ffffff;
    --card-silver: #e4e6e8;
    --blue-deep: #0f4f86;
    --blue-mid: #2369a6;
    --blue-ink: #1d5f9b;
    --green: #4f9a2c;
    --green-light: #8cc63f;
    --grey-text: #5d6166;
    --grey-soft: #b9bcc0;
  }
  * { margin: 0; padding: 0; box-sizing: border-box; }
  html, body { width: 1200px; height: 901px; overflow: hidden; }
  body {
    background: var(--bg);
    font-family: "Lora", Georgia, serif;
    display: flex;
    flex-direction: column;
    align-items: center;
    justify-content: center;
    gap: 40px;
  }
  .card {
    position: relative;
    width: 700px;
    height: 400px;
    border-radius: 22px;
    overflow: hidden;
    background: var(--card-white);
  }
  .card-front .wave { position: absolute; inset: 0; }
  .brand {
    position: absolute;
    left: 38px;
    top: 34px;
    display: flex;
    align-items: center;
    gap: 12px;
  }
  .brand-dot {
    width: 46px; height: 46px;
    border-radius: 50%;
    background: var(--blue-ink);
  }
  .brand-name {
    font-weight: 700;
    font-size: 36px;
    color: var(--blue-ink);
    letter-spacing: -0.5px;
  }
  .person { position: absolute; left: 40px; top: 120px; }
  .person-name { font-weight: 700; font-size: 28px; color: var(--blue-ink); line-height: 1.1; }
  .person-title { font-size: 17px; color: var(--grey-text); margin-top: 4px; }
  .contact {
    position: absolute;
    left: 435px;
    top: 236px;
    list-style: none;
    color: #fff;
    font-size: 15px;
  }
  .contact li { display: flex; align-items: center; gap: 10px; height: 25px; }
  .contact svg { width: 16px; height: 16px; flex: none; fill: #fff; }

  .card-back { background: linear-gradient(160deg, #ffffff 0%, var(--card-silver) 100%); }
  .back-mark {
    position: absolute;
    left: 70px;
    top: 130px;
    display: flex;
    align-items: center;
    gap: 22px;
  }
  .back-mark .brand-dot { width: 110px; height: 110px; background: var(--grey-soft); }
  .back-mark .brand-name { font-size: 52px; color: var(--grey-soft); }
  .back-url {
    position: absolute;
    right: 26px;
    top: 50%;
    transform: translateY(-50%) rotate(90deg);
    transform-origin: center;
    font-size: 15px;
    letter-spacing: 2px;
    color: var(--grey-text);
    white-space: nowrap;
    width: 20px;
    display: flex;
    justify-content: center;
  }
</style>
</head>
<body>

<section class="card card-front">
  <svg class="wave" viewBox="0 0 700 400" preserveAspectRatio="none" aria-hidden="true">
    <path d="M0 190 C160 250 330 250 470 215 C570 190 640 175 700 180 L700 198 C640 193 570 206 470 232 C330 268 160 268 0 212 Z" fill="var(--green)"/>
    <path d="M0 218 C160 275 330 278 470 243 C570 218 640 205 700 210 L700 400 L0 400 Z" fill="var(--blue-deep)"/>
    <path d="M0 235 C180 300 340 298 470 262 C570 236 640 224 700 228 L700 245 C640 242 580 252 480 280 C340 318 180 318 0 260 Z" fill="var(--blue-mid)" opacity="0.7"/>
  </svg>

  <div class="brand">
    <span class="brand-dot"></span>
    <span class="brand-name">Bluebird Hosting</span>
  </div>

  <div class="person">
    <div class="person-name">Mack Dorran</div>
    <div class="person-title">Service Director</div>
  </div>

  <ul class="contact">
    <li><svg viewBox="0 0 16 16"><path d="M8 1 L15 8 H13 V15 H10 V10 H6 V15 H3 V8 H1 Z"/></svg>Western Region</li>
    <li><svg viewBox="0 0 16 16"><path d="M4 1 L6.5 4 L5 6 C6 8.5 7.5 10 10 11 L12 9.5 L15 12 L13 15 C7 14 2 9 1 3 Z"/></svg>8005550142</li>
    <li><svg viewBox="0 0 16 16"><rect x="4" y="1" width="8" height="14" rx="1.5"/><rect x="5.5" y="3" width="5" height="8" fill="var(--blue-deep)"/></svg>8015550187</li>
    <li><svg viewBox="0 0 16 16"><rect x="1" y="6" width="14" height="8" rx="1"/><rect x="4" y="1" width="8" height="5"/></svg>18015550163</li>
    <li><svg viewBox="0 0 16 16"><rect x="1" y="3" width="14" height="10" rx="1"/><path d="M1.5 3.5 L8 9 L14.5 3.5" fill="none" stroke="var(--blue-deep)" stroke-width="1.5"/></svg>mack@mybluebirdhosting.com</li>
    <li><svg viewBox="0 0 16 16"><circle cx="8" cy="8" r="7"/><path d="M1 8 H15 M8 1 C4 5 4 11 8 15 M8 1 C12 5 12 11 8 15" fill="none" stroke="var(--blue-deep)" stroke-width="1"/></svg>mybluebirdhosting.com</li>
  </ul>
</section>

<section class="card card-back">
  <div class="back-mark">
    <span class="brand-dot"></span>
    <span class="brand-name">Bluebird Hosting</span>
  </div>
  <div class="back-url"><span>www.mybluebirdhosting.com</span></div>
</section>

</body>
</html>
```